Design some Business Cards for Quizwell

I would like to have a business card designed.

Use the logo from https://www.quizwell-demo.net - we're an education company, keep it elegant and simple; nothing too extravagant. Double Sided isn't necessary but could be better.

Name: Dov Renkel, Founder
Email: dov@quizwell-demo.net
Phone: 5550142986
website: https://www.quizwell-demo.net

Would like the slogan "Exam Management Made Easy" on the back if possible.

```html
<!DOCTYPE html>
<html lang="en">
<head>
<meta charset="utf-8">
<title>Quizwell Business Cards</title>
<link rel="stylesheet" href="https://fonts.googleapis.com/css2?family=Roboto:wght@300;400&display=swap">
<style>
  :root {
    --stage: #232425;
    --navy: #16284a;
    --white: #ffffff;
    --lime: #8be11f;
    --soft-text: #d9dee8;
  }
  * { margin: 0; padding: 0; box-sizing: border-box; }
  html, body {
    width: 1200px; height: 900px; overflow: hidden;
    background: var(--stage);
    font-family: "Roboto", sans-serif;
  }
  .stage { position: relative; width: 1200px; height: 900px; }

  .card { position: absolute; left: 316px; width: 540px; height: 329px; overflow: hidden; }

  /* Front */
  .card-front { top: 108px; background: var(--white); }
  .front-brand {
    position: absolute; top: 0; left: 0; width: 100%; height: 124px;
    display: flex; align-items: center; justify-content: center; gap: 14px;
    padding-top: 20px;
  }
  .brand-dot { display: block; }
  .brand-name-front {
    font-size: 54px; font-weight: 400; color: var(--navy); letter-spacing: 0.5px;
  }
  .contact-band {
    position: absolute; top: 124px; left: 0; width: 100%; height: 147px;
    background: var(--navy);
  }
  .contact-block { position: absolute; left: 173px; top: 27px; }
  .person { font-size: 17px; letter-spacing: 1.6px; margin-bottom: 8px; }
  .person-name { color: var(--lime); font-weight: 400; }
  .person-role { color: var(--soft-text); font-size: 14px; font-weight: 300; margin-left: 4px; }
  .contact-line {
    font-size: 14.5px; font-weight: 300; color: var(--soft-text);
    letter-spacing: 0.5px; line-height: 21px;
  }
  .contact-line .phone { letter-spacing: 2.4px; }

  /* Back */
  .card-back { top: 459px; background: var(--navy); }
  .back-brand {
    position: absolute; top: 132px; left: 0; width: 100%;
    display: flex; flex-direction: column; align-items: center;
  }
  .back-logo-row { display: flex; align-items: center; gap: 11px; }
  .brand-name-back { font-size: 38px; font-weight: 400; color: var(--white); }
  .slogan {
    margin-top: 2px; font-size: 13.5px; font-weight: 300; color: var(--soft-text);
    letter-spacing: 0.6px; text-transform: uppercase;
  }
</style>
</head>
<body>
<main class="stage">
  <section class="card card-front">
    <div class="front-brand">
      <svg class="brand-dot" width="40" height="40" viewBox="0 0 40 40" aria-hidden="true">
        <circle cx="20" cy="20" r="16" fill="none" stroke="var(--lime)" stroke-width="3"/>
      </svg>
      <span class="brand-name-front">Quizwell</span>
    </div>
    <div class="contact-band">
      <div class="contact-block">
        <p class="person"><span class="person-name">DOV RENKEL</span><span class="person-role">FOUNDER</span></p>
        <p class="contact-line">Phone : <span class="phone">555 014 2986</span></p>
        <p class="contact-line">Email &nbsp; : dov@quizwell-demo.net</p>
        <p class="contact-line">Website: www.quizwell-demo.net</p>
      </div>
    </div>
  </section>

  <section class="card card-back">
    <div class="back-brand">
      <div class="back-logo-row">
        <svg class="brand-dot" width="30" height="30" viewBox="0 0 30 30" aria-hidden="true">
          <circle cx="15" cy="15" r="12" fill="none" stroke="var(--lime)" stroke-width="2.4"/>
        </svg>
        <span class="brand-name-back">Quizwell</span>
      </div>
      <p class="slogan">Exam Management Made Easy</p>
    </div>
  </section>
</main>
</body>
</html>
```